Business Card Design for Vintage Jazz

I am a vintage jazz band leader in New York City. My groups play the music of the 1920s, 1930s and 1940s. My website is marlowpeskin.com for more info on what I do.

I am looking for a two sided business card design that has the look and feel of a really nice business card from the 1930s. I need to convey with the design that my work has that vintage kind of class and style, but also conveys that we are fun and entertaining.

Most importantly it should make a bold staement. If Hollis Varnum had a card, what would it have looked like? I want a card that I feel confident will make an impact and will let people know that my work is te the top that NYC has to offer in vintage jazz..

Note that I have only decided to avoid the "committed payment" option as I have not used this service before. Assuming that I get quality work I will select a design from those presented.

Target Market(s)

people who want to hire my band for events, media, and new fans of the band

Industry/Entity Type

Performing Art

Contact Information for Business Card

Definitely a matte finish, possibly a sort of old style of paper with that brown tint? definitely a thick card.

Requirements
Must have
• FRONT
• My name: Marlow Peskin
• What I do: Bandleader, Guitarist, Vocalist, Songwriter
• Contact Details: marlowpeskin.com marlow@marlowpeskin.com 646-555-0187
• BACK
• My Social Media Links:
• facebook.marlowpeskin.com
• twitter, instagram, linkedin: marlowpeskin
• I'm also including a photo image I would like to use. The photo's background is not needed, and to be honest isn't really desireable. Just looking to use the image of me.
Nice to have
• I'm attaching which could be used as is, omitted from the card, or altered maybe with text going around the outside of the circle or in some other way. It may need some clean up to the edges of the lettering as we only use it for the website thumbnail.
• If there's space I'd like to include the text "join our mailing list for a free song download: freesong.marlowpeskin.com" If not perhaps just "Download a Free Song at: freesong.marlowpeskin.com - something to this end.
Should not have
• anything cartoony. Don't think retro 90s's vision of the swing era, think actual swing era!
• anything modern. Got to look old school
• Try to avoid dark backgrounds. Since we often play in bars and clubs where it is dar, a d
• avoid script fonts.

```html
<!DOCTYPE html>
<html lang="en">
<head>
<meta charset="utf-8">
<title>Marlow Peskin – Business Card</title>
<link href="https://fonts.googleapis.com/css2?family=Questrial&family=Arimo:wght@400;700&display=swap" rel="stylesheet">
<style>
  :root {
    --page: #e9e6e1;
    --ink: #0b0b0b;
    --cream: #ede1bf;
    --cream-text: #e6d9b4;
    --teal: #4bbfa6;
    --paper-white: #f4f4f4;
    --grey-text: #d6d6d6;
    --photo-dark: #2a2a2a;
    --photo-light: #b9b9b9;
  }
  * { margin: 0; padding: 0; box-sizing: border-box; }
  html, body {
    width: 1200px; height: 902px; overflow: hidden;
    background: var(--page);
  }
  .canvas {
    position: relative; width: 1200px; height: 902px;
  }
  .card {
    position: absolute; left: 250px; width: 700px; height: 400px;
    overflow: hidden;
    box-shadow: 0 6px 18px rgba(0,0,0,0.18);
  }

  /* ---------- back side ---------- */
  .card-back { top: 38px; background: var(--ink); }
  .back-mark {
    position: absolute; left: 40px; top: 200px;
    display: flex; align-items: center; gap: 22px;
  }
  .back-mark-circle {
    width: 130px; height: 130px; border-radius: 50%;
    border: 10px solid var(--paper-white);
  }
  .back-mark-name {
    font-family: "Questrial", sans-serif;
    font-size: 44px; color: var(--paper-white);
    letter-spacing: 1px; line-height: 1.05;
  }
  .social {
    position: absolute; right: 40px; top: 36px;
    font-family: "Questrial", sans-serif;
    color: var(--grey-text); font-size: 30px;
  }
  .social-row {
    display: flex; align-items: center; justify-content: flex-end;
    gap: 12px; margin-bottom: 18px;
  }
  .social-row span { margin-right: 10px; }
  .social-square {
    width: 34px; height: 34px; background: var(--paper-white);
    border-radius: 3px;
  }

  /* ---------- front side ---------- */
  .card-front { top: 464px; background: var(--cream); }
  .name-band {
    position: absolute; left: 300px; right: 0; top: 58px; height: 84px;
    background: var(--ink);
  }
  .name {
    position: absolute; right: 34px; top: 78px;
    font-family: "Questrial", sans-serif;
    font-size: 44px; color: var(--cream-text); letter-spacing: 0.5px;
  }
  .portrait {
    position: absolute; left: 40px; top: 40px; width: 350px; height: 350px;
  }
  .roles {
    position: absolute; right: 34px; top: 168px; text-align: right;
    font-family: "Arimo", sans-serif; font-weight: 700;
    font-size: 24px; line-height: 1.2; color: var(--ink);
  }
  .contacts {
    position: absolute; right: 34px; top: 258px;
    font-family: "Arimo", sans-serif; font-size: 21px;
    color: var(--ink); list-style: none;
  }
  .contacts li {
    display: flex; align-items: center; justify-content: flex-end;
    gap: 10px; line-height: 1.35;
  }
  .contact-icon { width: 16px; height: 16px; flex: none; }
</style>
</head>
<body>
<main class="canvas">

  <section class="card card-back" aria-label="Card back">
    <div class="social">
      <div class="social-row"><span>marlowpeskin.com</span><div class="social-square"></div></div>
      <div class="social-row"><span>marlowpeskin</span><div class="social-square"></div><div class="social-square"></div><div class="social-square"></div></div>
    </div>
    <div class="back-mark">
      <div class="back-mark-circle"></div>
      <div class="back-mark-name">Marlow<br>Peskin</div>
    </div>
  </section>

  <section class="card card-front" aria-label="Card front">
    <div class="name-band"></div>
    <div class="name">Marlow Peskin</div>

    <svg class="portrait" viewBox="0 0 350 350" aria-hidden="false">
      <defs>
        <clipPath id="portrait-clip"><circle cx="175" cy="175" r="175"/></clipPath>
        <linearGradient id="portrait-tone" x1="0" y1="0" x2="0" y2="1">
          <stop offset="0" stop-color="var(--photo-light)"/>
          <stop offset="1" stop-color="var(--photo-dark)"/>
        </linearGradient>
      </defs>
      <circle cx="175" cy="175" r="175" fill="var(--teal)"/>
      <g clip-path="url(#portrait-clip)" role="img" aria-label="Black and white photo of the bandleader in a piped blazer, tipping a straw boater hat">
        <rect x="60" y="20" width="230" height="330" rx="90" fill="url(#portrait-tone)"/>
      </g>
    </svg>

    <div class="roles">Bandleader, Guitarist,<br>Vocalist, Songwriter</div>

    <ul class="contacts">
      <li>646-555-0187
        <svg class="contact-icon" viewBox="0 0 16 16" aria-hidden="true"><rect width="16" height="16" rx="2" fill="var(--ink)"/><path d="M5 3.5c-1 .6-1.3 2 .2 4.3s3.4 3.8 4.6 3.2l1-1-1.8-1.6-.9.6c-.6-.3-1.6-1.4-2-2.2l.6-.9L5.2 4z" fill="var(--cream)"/></svg>
      </li>
      <li>marlowpeskin.com
        <svg class="contact-icon" viewBox="0 0 16 16" aria-hidden="true"><rect width="16" height="16" rx="2" fill="var(--ink)"/><circle cx="8" cy="8" r="4.8" fill="none" stroke="var(--cream)" stroke-width="1.2"/><path d="M3.2 8h9.6M8 3.2c-2 2.6-2 7 0 9.6M8 3.2c2 2.6 2 7 0 9.6" fill="none" stroke="var(--cream)" stroke-width="1"/></svg>
      </li>
      <li>marlow@marlowpeskin.com
        <svg class="contact-icon" viewBox="0 0 16 16" aria-hidden="true"><rect width="16" height="16" rx="2" fill="var(--ink)"/><rect x="3" y="4.5" width="10" height="7" fill="var(--cream)"/><path d="M3 4.5l5 4 5-4" fill="none" stroke="var(--ink)" stroke-width="1"/></svg>
      </li>
    </ul>
  </section>

</main>
</body>
</html>
```